Marcus Feldwick Carpentry & Joinery

Hello, I would like a flyer designed for my new business doing small projects in my local area for home-owners. I am a professional tradesman.
The type of work I am offering is:
- decks/decking
- external stairs & railings
- install windows & doors
- roofs & gutters
- small additions
- built-in wardrobes
- finish work
- demolition

It would be great if the flyer could mention these, or use phrasing that fits this kind of construction work.
My idea for a slogan was "new work and repairs to any age home".

Please also mention FREE QUOTES and have my email and phone number included on the flyer, along with my carpentry licence number, which I can provided.

I'd like a one page, single-sided flyer that could be printed as DL.
Colour and style is up to you! I'll be placing this flyer on counters & in the windows of local businesses, so something simple and eye-catching is preferred.

Thank you!

```html
<!DOCTYPE html>
<html lang="en">
<head>
<meta charset="utf-8">
<title>New Work and Repairs – Flyer</title>
<link href="https://fonts.googleapis.com/css2?family=Lato:wght@300;400;700&display=swap" rel="stylesheet">
<style>
  :root {
    --yellow: #f2c518;
    --yellow-deep: #e9b80e;
    --charcoal: #4a4a4c;
    --headline-yellow: #f7d95a;
    --white: #ffffff;
    --text-dark: #3d3d3f;
    --shadow-grey: #e6e3da;
  }
  html, body {
    margin: 0;
    padding: 0;
    overflow: hidden;
  }
  body {
    width: 849px;
    height: 1200px;
    font-family: "Lato", Arial, sans-serif;
  }
  .flyer {
    position: relative;
    width: 849px;
    height: 1200px;
    overflow: hidden;
    background: radial-gradient(ellipse at 40% 40%, var(--yellow) 0%, var(--yellow) 55%, var(--yellow-deep) 100%);
  }
  .headline {
    position: absolute;
    left: 186px;
    top: 0;
    width: 477px;
    height: 267px;
    background: var(--charcoal);
    text-align: center;
    font-weight: 300;
    box-sizing: border-box;
    padding-top: 28px;
  }
  .headline .main {
    color: var(--headline-yellow);
    font-size: 76px;
    line-height: 76px;
    display: block;
  }
  .headline .sub {
    color: var(--white);
    font-size: 54px;
    line-height: 70px;
    display: block;
  }
  .gallery {
    position: absolute;
    left: 72px;
    top: 267px;
    width: 705px;
    height: 467px;
    background: var(--white);
    box-shadow: 0 6px 14px rgba(0,0,0,0.25);
  }
  .photo {
    position: absolute;
    width: 220px;
    height: 220px;
  }
  .photo.c1 { left: 10px; }
  .photo.c2 { left: 239px; width: 224px; }
  .photo.c3 { left: 476px; }
  .photo.r1 { top: 10px; }
  .photo.r2 { top: 238px; }
  .photo.bathroom { background: linear-gradient(160deg, #f1f1ef 0%, #d9dbd8 55%, #bfbcb4 100%); }
  .photo.kitchen-steel { background: linear-gradient(90deg, #a96c34 0%, #c7c9c8 30%, #9fa3a3 55%, #8a5428 80%, #c98a4c 100%); }
  .photo.roofline { background: linear-gradient(180deg, #6b9fd2 0%, #a9c8e6 60%, #d9a36f 82%, #f0d9a0 100%); }
  .photo.tools { background: linear-gradient(135deg, #b98a56 0%, #d9b07a 50%, #9d9c96 100%); }
  .photo.kitchen-wood { background: linear-gradient(180deg, #8c4d20 0%, #b06a2c 40%, #d8c9a8 60%, #c47a34 100%); }
  .photo.house-front { background: linear-gradient(180deg, #e9e0c4 0%, #f0e3a8 50%, #5f9a3a 78%, #c49a6c 100%); }
  .services {
    position: absolute;
    left: 73px;
    top: 766px;
    color: var(--text-dark);
    font-weight: 400;
    font-size: 28px;
    letter-spacing: 0.4px;
    line-height: 34.2px;
  }
  .services p { margin: 0; }
  .services ul {
    list-style: none;
    margin: 0;
    padding: 0;
  }
  .services li::before {
    content: "";
    display: inline-block;
    width: 9px;
    height: 9px;
    border-radius: 50%;
    background: var(--text-dark);
    margin: 0 9px 4px 3px;
    vertical-align: middle;
  }
  .quote-badge {
    position: absolute;
    left: 542px;
    top: 770px;
    width: 235px;
    height: 235px;
    border-radius: 50%;
    background: var(--charcoal);
    color: var(--headline-yellow);
    text-align: center;
    font-weight: 300;
    box-sizing: border-box;
    padding-top: 62px;
    z-index: 2;
  }
  .quote-badge .free { display: block; font-size: 80px; line-height: 78px; }
  .quote-badge .quotes { display: block; font-size: 48px; line-height: 38px; }
  .badge-shadow {
    position: absolute;
    left: 572px;
    top: 988px;
    width: 178px;
    height: 25px;
    border-radius: 50%;
    background: var(--shadow-grey);
    z-index: 1;
  }
  .contact-bar {
    position: absolute;
    left: 0;
    top: 1095px;
    width: 849px;
    height: 105px;
    background: var(--charcoal);
    color: var(--white);
    font-weight: 300;
    font-size: 29px;
  }
  .contact-lines {
    position: absolute;
    left: 74px;
    top: 14px;
    line-height: 37px;
  }
  .contact-lines .value {
    color: var(--headline-yellow);
    font-weight: 700;
    letter-spacing: 1.5px;
  }
  .divider {
    position: absolute;
    left: 469px;
    top: 12px;
    height: 86px;
    border-left: 2px dotted #bdbdbd;
  }
  .licence {
    position: absolute;
    left: 511px;
    top: 14px;
    line-height: 37px;
  }
</style>
</head>
<body>
<main class="flyer">
  <header class="headline">
    <span class="main">New Work<br>and Repairs</span>
    <span class="sub">to any Age Home</span>
  </header>

  <section class="gallery">
    <div class="photo c1 r1 bathroom" role="img" aria-label="Renovated modern bathroom with glass shower"></div>
    <div class="photo c2 r1 kitchen-steel" role="img" aria-label="Kitchen with stainless steel fridge and oven"></div>
    <div class="photo c3 r1 roofline" role="img" aria-label="Tiled roof against a blue sky"></div>
    <div class="photo c1 r2 tools" role="img" aria-label="Hammer, nails, tape measure and wrench on timber"></div>
    <div class="photo c2 r2 kitchen-wood" role="img" aria-label="Timber kitchen cabinetry with dishwasher"></div>
    <div class="photo c3 r2 house-front" role="img" aria-label="Front of a home with columns and lawn"></div>
  </section>

  <section class="services">
    <p>The work offering are:</p>
    <ul>
      <li>Decks/decking</li>
      <li>External stairs &amp; railings</li>
      <li>Install windows &amp; doors</li>
      <li>Roofs &amp; gutters</li>
      <li>Small additions</li>
      <li>Built-in wardrobes</li>
      <li>Finish work</li>
      <li>Demolition</li>
    </ul>
  </section>

  <div class="quote-badge">
    <span class="free">FREE</span>
    <span class="quotes">QUOTES</span>
  </div>
  <div class="badge-shadow"></div>

  <footer class="contact-bar">
    <div class="contact-lines">
      <div>Call at : <span class="value">xxxxxxxxxxxxx</span></div>
      <div>Email at : <span class="value">xxxxxxxxxxxx</span></div>
    </div>
    <div class="divider"></div>
    <div class="licence">Licence No.:</div>
  </footer>
</main>
</body>
</html>
```